Animal Horse & Bedding Company Needs a Website Coded & Designed

We need a website for a new animal bedding and feed company that is visually grabbing and vibrant. We would like to see a website that displays trust, quality and confidence. Needs to be responsive and mobile friendly for all browsers and coded for both Android & IOS. SEO is also important.

Joomla or Wordpress – must be both desktop and mobile friendly with fast page load speed. Need the ability to edit ourselves in Wordpress or Joomla.

Full details attached below with some layout and content ideas.

Coding

Coded - Design and coding required

Number of Pages Required

5+ page

Font styles to use
Sans Serif

Requirements
Must have
• Needs to be responsive and mobile friendly for all browsers and coded for both Android & IOS. SEO is also important.

Wordpress – must be both desktop and mobile friendly with fast page load speed. Need the ability to edit ourselves in Wordpress.

Logo Colours:
Dark Brown
CMYK: 50 / 70 / 80 / 70
Pantone: 4625C

Orange
CMYK: 0 / 50 / 100 / 0
Pantone: 144C
Nice to have
• Use picture of building attached and super impose logo on building.

```html
<!DOCTYPE html>
<html lang="en">
<head>
<meta charset="utf-8">
<title>Golden Sheaf – Bedding</title>
<link rel="stylesheet" href="https://fonts.googleapis.com/css2?family=Montserrat:wght@400;500;600;700;800&display=swap">
<style>
:root{
  --orange:#f7931e;
  --brown:#3b2314;
  --ink:#111111;
  --text:#333333;
  --muted:#8a8a8a;
  --line:#d9d9d9;
  --soft:#f4f4f4;
  --white:#ffffff;
}
*{box-sizing:border-box;margin:0;padding:0}
html,body{width:1200px;height:2846px;overflow:hidden}
body{font-family:'Montserrat',sans-serif;color:var(--text);background:var(--white);position:relative}
.abs{position:absolute}

/* header */
.site-header{position:absolute;left:0;top:0;width:1200px;height:62px;background:var(--white);border-bottom:1px solid #eee}
.brand{position:absolute;left:172px;top:18px;display:flex;align-items:center;gap:8px}
.brand-dot{width:22px;height:22px;border-radius:50%;background:var(--orange)}
.brand-name{font-weight:700;font-size:18px;color:var(--brown);letter-spacing:1px;text-transform:uppercase}
.main-nav{position:absolute;left:546px;top:24px;display:flex;gap:32px;font-size:13px;color:var(--text)}
.main-nav .active{color:var(--orange);position:relative}
.main-nav .active::after{content:"";position:absolute;left:50%;bottom:-7px;width:16px;height:2px;margin-left:-8px;background:var(--orange)}
.btn{display:inline-flex;align-items:center;justify-content:center;background:var(--orange);color:var(--white);font-weight:700;border-radius:2px}
.header-cta{position:absolute;left:923px;top:18px;width:104px;height:28px;font-size:12px}

/* hero */
.hero{position:absolute;left:0;top:62px;width:1200px;height:344px;
  background:linear-gradient(90deg,#0b0a07 0%,#1d1a10 12%,#4a3b16 30%,#8b6420 50%,#3d4a1f 70%,#5a6a2a 85%,#a3551a 100%)}
.hero-title{position:absolute;left:173px;top:74px;font-size:50px;font-weight:700;color:var(--white)}
.hero-text{position:absolute;left:172px;top:152px;width:300px;font-size:16px;line-height:17px;color:var(--white)}
.hero-cta{position:absolute;left:172px;top:228px;width:105px;height:28px;font-size:12px}

/* intro */
.section-title{position:absolute;left:0;width:1200px;text-align:center;font-size:26px;font-weight:700;color:var(--ink)}
.intro-sub{position:absolute;left:0;top:541px;width:1200px;text-align:center;font-size:15px;font-weight:600;color:var(--orange)}
.intro-copy{position:absolute;left:270px;top:568px;width:660px;text-align:center;font-size:10.5px;line-height:15px;color:var(--muted)}
.intro-copy p+p{margin-top:15px}
.feature-photo{position:absolute;left:172px;top:684px;width:855px;height:368px;border-radius:4px;
  background:linear-gradient(180deg,#c9ccd0 0%,#9aa0a4 40%,#b8542b 70%,#8e9194 100%)}

/* benefits */
.benefit{position:absolute;width:180px;text-align:center}
.benefit svg{display:block;margin:0 auto 10px}
.benefit-label{font-size:12.5px;font-weight:600;line-height:13px;color:var(--ink)}

/* quote */
.quote-band{position:absolute;left:0;top:1482px;width:1200px;height:625px;background:var(--soft)}
.quote-card{position:absolute;left:172px;top:98px;width:855px;height:430px;background:var(--white);border:1px solid var(--line);border-radius:8px}
.quote-title{position:absolute;left:0;top:36px;width:100%;text-align:center;font-size:26px;font-weight:700;color:var(--ink)}
.field{position:absolute;border:1px solid var(--line);border-radius:3px;font-size:10px;color:#aaa;padding:13px 15px}
.send-btn{position:absolute;left:336px;top:354px;width:197px;height:36px;font-size:12.5px}

/* testimonials */
.testimonials{position:absolute;left:0;top:2107px;width:1200px;height:421px;
  background:radial-gradient(ellipse at 85% 40%,#5a4a36 0%,#352b1f 45%,#231c14 100%)}
.t-title{position:absolute;left:0;top:98px;width:100%;text-align:center;font-size:25px;font-weight:700;color:var(--white)}
.t-name{position:absolute;left:0;top:160px;width:100%;text-align:center;font-size:15px;font-weight:600;color:var(--white)}
.t-role{position:absolute;left:0;top:180px;width:100%;text-align:center;font-size:10px;color:var(--white)}
.t-quote{position:absolute;left:350px;top:213px;width:500px;text-align:center;font-size:10px;line-height:15px;color:var(--white)}
.t-arrow{position:absolute;top:237px}
.t-dots{position:absolute;left:579px;top:308px;display:flex;gap:6px}
.t-dots span{width:9px;height:9px;border-radius:50%;border:1px solid var(--white)}
.t-dots .on{background:var(--white)}

/* footer */
.site-footer{position:absolute;left:0;top:2528px;width:1200px;height:318px;background:var(--white)}
.footer-brand{position:absolute;left:172px;top:87px;display:flex;align-items:center;gap:8px}
.footer-about{position:absolute;left:172px;top:164px;width:165px;font-size:9px;line-height:11px;color:var(--muted)}
.f-head{position:absolute;top:88px;font-size:14.5px;font-weight:600;color:var(--ink)}
.f-list{position:absolute;top:123px;font-size:9px;line-height:21.5px;color:var(--muted);list-style:none}
.f-contact{position:absolute;left:604px;top:123px;font-size:9px;line-height:13px;color:var(--muted)}
.f-contact p+p{margin-top:8px}
.socials{position:absolute;left:830px;top:118px;display:flex;gap:13px}
.socials span{width:9px;height:9px;border-radius:50%;background:var(--muted)}
.socials span:nth-child(2){background:var(--orange)}
.sub-email{position:absolute;left:830px;top:154px;width:196px;height:25px;border:1px solid #eee;font-size:9px;color:#bbb;padding:7px 0 0 29px}
.sub-email::before{content:"";position:absolute;left:10px;top:8px;width:8px;height:8px;background:var(--orange);border-radius:2px}
.sub-btn{position:absolute;left:830px;top:188px;width:196px;height:26px;font-size:9px;font-weight:500}
.copyright{position:absolute;left:0;top:269px;width:1200px;border-top:1px solid #e6e6e6;text-align:center;font-size:9px;color:var(--text);padding-top:16px;height:49px}
</style>
</head>
<body>

<header class="site-header">
  <div class="brand"><span class="brand-dot"></span><span class="brand-name">Golden Sheaf</span></div>
  <nav class="main-nav">
    <span>Home</span><span>About Us</span><span>Feed</span><span class="active">Bedding</span><span>Contact</span>
  </nav>
  <span class="btn header-cta">Get a Quote</span>
</header>

<section class="hero" role="img" aria-label="Rabbit sitting on a tree stump beside a pumpkin and autumn leaves">
  <h1 class="hero-title">Bedding</h1>
  <p class="hero-text">Golden Sheaf offers supply and delivery of fresh bedding as well as removal of waste bedding.</p>
  <span class="btn hero-cta">Get a Quote</span>
</section>

<h2 class="section-title" style="top:496px">Bedding</h2>
<p class="intro-sub">Clean, dry, natural solution</p>
<div class="intro-copy">
  <p>For many people, their animals, whether it be a horse, goat or other are more than just an animal, they are a part of your family, a way of life, and their comfort is important. Fine cut 100% chopped straw offers a softer bedding for your equine or other large and/or small animal.</p>
  <p>This straw bedding is light weight which allows for easier spreading, removing and hauling away. Straw also decomposes a lot faster than wood shavings and makes for great compost material.</p>
</div>
<div class="feature-photo" role="img" aria-label="Pigs in metal barn pens with orange floor mats"></div>

<h2 class="section-title" style="top:1104px">Benefits</h2>

<div class="benefit" style="left:292px;top:1175px">
  <svg width="46" height="46" viewBox="0 0 46 46"><circle cx="23" cy="23" r="22" fill="#f7931e"/><circle cx="23" cy="23" r="16" fill="none" stroke="#fff" stroke-width="1.5"/><text x="23" y="27" text-anchor="middle" font-family="Montserrat,sans-serif" font-size="11" font-weight="700" fill="#fff">100%</text></svg>
  <div class="benefit-label">100% Natural<br>Chopped Straw</div>
</div>
<div class="benefit" style="left:513px;top:1175px">
  <svg width="50" height="46" viewBox="0 0 50 46"><path d="M2 10l6-8 6 8v34H2zM19 10l6-8 6 8v34H19zM36 10l6-8 6 8v34H36z" fill="#f7931e"/><rect x="2" y="16" width="46" height="6" fill="#f7931e"/><rect x="2" y="32" width="46" height="6" fill="#f7931e"/></svg>
  <div class="benefit-label">Cheaper than<br>Wood Shavings</div>
</div>
<div class="benefit" style="left:734px;top:1175px">
  <svg width="42" height="46" viewBox="0 0 42 46"><path d="M14 4h14l-4 8c10 4 16 14 16 24 0 6-4 8-8 8H10c-4 0-8-2-8-8 0-10 6-20 16-24z" fill="#f7931e"/></svg>
  <div class="benefit-label">less used and<br>less wasted</div>
</div>
<div class="benefit" style="left:292px;top:1300px">
  <svg width="46" height="46" viewBox="0 0 46 46"><rect x="4" y="2" width="6" height="16" fill="#f7931e"/><rect x="0" y="18" width="16" height="26" fill="#f7931e"/><rect x="24" y="2" width="20" height="14" fill="#f7931e"/><rect x="30" y="16" width="8" height="28" fill="#f7931e"/></svg>
  <div class="benefit-label">Clean &amp; Highly<br>Absorbent</div>
</div>
<div class="benefit" style="left:513px;top:1300px">
  <svg width="46" height="46" viewBox="0 0 46 46"><circle cx="23" cy="23" r="20" fill="none" stroke="#f7931e" stroke-width="4"/><line x1="9" y1="37" x2="37" y2="9" stroke="#f7931e" stroke-width="4"/><circle cx="23" cy="23" r="7" fill="#f7931e"/></svg>
  <div class="benefit-label">Chemical &amp;<br>Additive Free</div>
</div>
<div class="benefit" style="left:734px;top:1300px">
  <svg width="40" height="46" viewBox="0 0 40 46"><rect x="14" y="0" width="12" height="5" fill="#f7931e"/><rect x="2" y="5" width="36" height="6" fill="#f7931e"/><path d="M5 13h30l-3 33H8z" fill="#f7931e"/><circle cx="20" cy="29" r="7" fill="none" stroke="#fff" stroke-width="2.5"/></svg>
  <div class="benefit-label">Recyclable &amp;<br>Compostable</div>
</div>

<section class="quote-band">
  <div class="quote-card">
    <h2 class="quote-title">Request a Quote</h2>
    <div class="field" style="left:38px;top:95px;width:381px;height:38px">First Name*</div>
    <div class="field" style="left:436px;top:95px;width:381px;height:38px">Last Name*</div>
    <div class="field" style="left:38px;top:144px;width:381px;height:38px">Email Address*</div>
    <div class="field" style="left:436px;top:144px;width:381px;height:38px">Contact Number*</div>
    <div class="field" style="left:38px;top:195px;width:779px;height:139px">Requirements*</div>
    <span class="btn send-btn">Send Message</span>
  </div>
</section>

<section class="testimonials" role="img" aria-label="Lambs standing in a field at dusk">
  <h2 class="t-title">Whats Our Clients Says</h2>
  <p class="t-name">Daniel Hartley</p>
  <p class="t-role">Managing Member, Northfield Holdings</p>
  <p class="t-quote">Lorem Ipsum is simply dummy text of the printing and typesetting industry. Lorem Ipsum has been the industry's standard dummy text ever since the 1500s, when an unknown printer took a galley of type and scrambled it to make a type specimen book. It has survived not only five centuries, but also the leap into electronic typesetting, remaining essentially unchanged.</p>
  <svg class="t-arrow" style="left:247px" width="10" height="16" viewBox="0 0 10 16"><path d="M8 1L2 8l6 7" fill="none" stroke="#fff" stroke-width="1.5"/></svg>
  <svg class="t-arrow" style="left:943px" width="10" height="16" viewBox="0 0 10 16"><path d="M2 1l6 7-6 7" fill="none" stroke="#fff" stroke-width="1.5"/></svg>
  <div class="t-dots"><span></span><span></span><span class="on"></span></div>
</section>

<footer class="site-footer">
  <div class="footer-brand"><span class="brand-dot"></span><span class="brand-name" style="font-size:16px">Golden Sheaf</span></div>
  <p class="footer-about">Ready to start a new project or curious about our process? Drop us a note or give us a call. We are happy to answer any questions and provide a free consultation.</p>

  <h3 class="f-head" style="left:434px">Menu</h3>
  <ul class="f-list" style="left:435px"><li>Home</li><li>About us</li><li>Feed</li><li>Badding</li><li>Contact</li></ul>

  <h3 class="f-head" style="left:604px">Contact Us</h3>
  <div class="f-contact">
    <p>Golden Sheaf<br>118 Meadow Lane #22, Millbrook,<br>VT 05401</p>
    <p>555-014-2380</p>
    <p>hello@goldensheaf.com</p>
  </div>

  <h3 class="f-head" style="left:830px">Social Media</h3>
  <div class="socials"><span></span><span></span><span></span><span></span><span></span></div>
  <div class="sub-email">Email Address</div>
  <span class="btn sub-btn">Subscribe Now</span>

  <p class="copyright">©2021 goldensheaf. All Rights Reserved.</p>
</footer>

</body>
</html>
```